Business Consultancy Wordpress Design

Small business analysis consultancy.

Looking for a bold, clean design for Wordpress. Final site will only be a few pages, some contact information, services provided and a little background information. Potentially a blog.

Colours to be as per logo, with either black or white as the main colour.

Link is www.brevikadvisory.com

More details to be included in the best few days

Name - Brevik Advisory
Provides - Project Consultancy
Updates

Project Deadline Extended
Reason: I am going to be on holiday with little access to the web over 28/02 - 05/03 and am therefore extending the deadline

Target Market(s)

Business professionals

Industry/Entity Type

Business

Colors

Designer to choose colors to be used in the design.

Requirements
Must have
• Must contain the logo in the header
Footer must fit a 3 column layout in wordpress

Business style, royalty free stock images
Nice to have
• Would like the 1 or 2 column wordpress style layout
Should not have
• must not be blog or magazine style layout or look and feel

```html
<!DOCTYPE html>
<html lang="en">
<head>
<meta charset="utf-8">
<title>Brevik Advisory</title>
<link href="https://fonts.googleapis.com/css2?family=PT+Sans:ital,wght@0,400;0,700;1,400&family=Oswald:wght@400&family=Roboto+Condensed:wght@400&display=swap" rel="stylesheet">
<style>
:root{
  --black:#000;
  --ink:#1b1b1b;
  --grey:#777;
  --rule:#d6d6d6;
  --blue:#0fa3de;
  --link:#1e7fbf;
  --green:#76bd3a;
  --white:#fff;
  --footer-base:#161616;
}
*{margin:0;padding:0;box-sizing:border-box}
html,body{width:1032px;height:1200px;overflow:hidden;background:var(--white)}
body{position:relative;font-family:"PT Sans",sans-serif;color:var(--ink)}
.abs{position:absolute}

.site-header{left:0;top:0;width:1032px;height:77px;background:var(--black)}
.brand{left:123px;top:22px;display:flex;align-items:center;gap:8px;color:#bdbdbd;font-size:20px;letter-spacing:.3px}
.brand-dot{width:28px;height:28px;border-radius:50%;background:var(--blue)}
.phone{right:129px;top:28px;color:var(--green);font-size:13px}
.phone b{font-weight:400;font-size:17px}

.main-nav{left:0;top:77px;width:1032px;height:43px;background:var(--blue)}
.main-nav ul{list-style:none;position:absolute;left:114px;top:13px;display:flex;gap:27px}
.main-nav li{color:var(--white);font-size:13px}
.search{right:115px;top:6px;width:172px;height:29px;background:var(--white);border-radius:15px;font-size:11px;color:#555;padding:8px 0 0 14px}
.search svg{position:absolute;right:10px;top:6px}

.hero{left:0;top:120px;width:1032px;height:374px;background:
  linear-gradient(180deg,rgba(0,0,0,0) 62%,rgba(178,154,124,.85) 82%,#8b7560 100%),
  linear-gradient(100deg,#5e8c34 0%,#86b04e 40%,#9cc061 65%,#6f9a3c 100%)}
.hero-title{left:451px;top:263px;font-family:"Oswald",sans-serif;font-size:28px;color:var(--white);letter-spacing:-.3px}
.hero-sub{left:644px;top:303px;font-style:italic;font-size:13px;color:#222}
.slider-arrows{left:479px;top:439px}

.content{left:86px;top:494px;width:860px;height:460px;background:var(--white);box-shadow:0 0 4px rgba(0,0,0,.18)}
.feature{top:20px}
.feature-head{display:flex;align-items:center;gap:10px}
.feature-title{font-size:15px;font-weight:700;line-height:1;letter-spacing:-.3px}
.feature-title small{display:block;font-size:7.5px;font-weight:400;letter-spacing:.2px;margin-top:2px}
.lead{color:var(--green);font-size:11.5px;line-height:14.5px}
.body-text{color:var(--grey);font-size:11px;line-height:14.5px}
.body-text b{color:var(--ink);font-style:italic}
.underline{color:var(--ink);font-size:11px;text-decoration:underline}
.more{display:inline-block;width:83px;height:14px;background:linear-gradient(#555,#222);color:var(--white);font-size:11px;line-height:14px;text-align:center;border-radius:1px}
.vrule{top:32px;width:1px;height:160px;background:var(--rule)}
.hrule{left:20px;top:192px;width:824px;height:1px;background:var(--rule)}
.links{list-style:none}
.links li{font-size:11px;color:var(--link);text-decoration:underline;height:19px;display:flex;align-items:center;gap:9px}
.section-title{font-family:"Roboto Condensed",sans-serif;font-size:17px;color:var(--ink)}
.about p{font-size:10.4px;line-height:20.6px;color:#444;width:512px;margin-bottom:20px}
.post{display:flex;gap:10px;width:240px}
.post-text{width:150px}
.thumb{width:53px;height:53px;border:1px solid #ccc;padding:2px;flex:none}
.thumb div{width:100%;height:100%}
.post h4{font-weight:400;font-size:12.5px;line-height:14px;white-space:nowrap}
.post p{font-size:9.8px;line-height:13px;color:#333;width:140px}

.site-footer{left:0;top:954px;width:1032px;height:214px;background:var(--black);color:var(--white)}
.foot-title{font-size:15.5px;letter-spacing:.3px}
.quick ul{list-style:none;margin-top:16px}
.quick li{font-size:13px;height:24px;display:flex;align-items:center;gap:7px}
.email{width:230px;height:31px;background:var(--white);border-radius:4px;color:#999;font-size:13px;padding:7px 14px}
.note{font-size:10px;line-height:13.5px;width:230px}
.submit{width:75px;height:21px;background:var(--blue);border-radius:2px;text-align:center;font-size:12.5px;line-height:21px}
.social{display:flex;gap:10px}
.social span{width:33px;height:33px;border-radius:4px}
.faint-brand{left:705px;top:1105px;display:flex;align-items:center;gap:6px;color:#2a2a2a;font-size:16px}
.faint-brand i{width:22px;height:22px;border-radius:50%;background:#1f1f1f}
.bottom-bar{left:0;top:1168px;width:1032px;height:32px;background:var(--footer-base);color:#ddd;font-size:10px;text-align:center;line-height:32px}
</style>
</head>
<body>

<header class="site-header abs">
  <div class="brand abs"><span class="brand-dot"></span>BREVIK ADVISORY</div>
  <div class="phone abs">Call Us : <b>1800 . 461 . 3075</b></div>
</header>

<nav class="main-nav abs">
  <ul><li>Home</li><li>About Us</li><li>Services</li><li>Blog</li><li>Newsletter</li><li>Contact Us</li></ul>
  <div class="search abs">Search
    <svg width="18" height="18" viewBox="0 0 18 18"><circle cx="7.5" cy="7.5" r="6" fill="none" stroke="#777" stroke-width="1.6"/><line x1="12" y1="12" x2="16.5" y2="16.5" stroke="#777" stroke-width="1.8"/></svg>
  </div>
</nav>

<section class="hero abs" role="img" aria-label="Photo of a small globe resting on a log against a soft green grass background"></section>
<h1 class="hero-title abs" style="font-weight:400">We provide business consulting services</h1>
<p class="hero-sub abs">Aenean nonummy hendrerit mauris.</p>
<svg class="slider-arrows abs" width="74" height="36" viewBox="0 0 74 36">
  <circle cx="17" cy="18" r="17" fill="rgba(70,60,50,.55)"/><circle cx="56" cy="18" r="17" fill="rgba(70,60,50,.55)"/>
  <path d="M20 11 L13 18 L20 25Z" fill="#fff"/><path d="M53 11 L60 18 L53 25Z" fill="#fff"/>
</svg>

<main class="content abs">
  <div class="feature abs" style="left:20px;width:245px">
    <div class="feature-head">
      <svg width="42" height="42" viewBox="0 0 42 42"><defs><radialGradient id="g1" cx=".35" cy=".3"><stop offset="0" stop-color="#fff"/><stop offset="1" stop-color="#7c7c7c"/></radialGradient></defs><circle cx="21" cy="21" r="20" fill="url(#g1)"/></svg>
      <div class="feature-title">GLOBALIZATION<small>LOREM IPSUM DOLOR</small></div>
    </div>
    <p class="lead" style="margin-top:15px">Sed posuere ligula rhoncus erat pulvinar quis, tincidunt et, risus.</p>
    <p style="margin-top:13px"><span class="underline">Morbi volutpat leo in ligula. Integer vel</span></p>
    <p class="body-text">magna. Nam justo augue, dictum a.<br>Morbi volutpat leo in Quisque ut</p>
    <span class="more" style="margin-top:3px">read more</span>
  </div>
  <div class="vrule abs" style="left:287px"></div>

  <div class="feature abs" style="left:314px;width:226px">
    <div class="feature-head">
      <svg width="40" height="40" viewBox="0 0 40 40"><g fill="#9a9a9a"><circle cx="20" cy="20" r="14"/><rect x="17" y="1" width="6" height="38"/><rect x="1" y="17" width="38" height="6"/><rect x="17" y="1" width="6" height="38" transform="rotate(45 20 20)"/><rect x="17" y="1" width="6" height="38" transform="rotate(-45 20 20)"/></g><circle cx="20" cy="20" r="9" fill="#e6e6e6"/><circle cx="20" cy="20" r="5" fill="#9a9a9a"/></svg>
      <div class="feature-title">INDUSTRIES<small>LOREM IPSUM DOLOR</small></div>
    </div>
    <p class="lead" style="margin-top:16px">Sed posuere ligula rhoncus erat</p>
    <p class="body-text">ultricies in, leo. Nullam eleifend. Duis tempor ipsum <b><u>vitae diam</u></b>. Curabitur felis dui, bibendum vitae, luctus quis, volutpat sed, orci. Cras vulputate ullamcorper ante. ultricies in, leo.</p>
    <span class="more" style="margin-top:3px">read more</span>
  </div>
  <div class="vrule abs" style="left:572px"></div>

  <div class="feature abs" style="left:598px;width:250px">
    <div class="feature-head">
      <svg width="42" height="40" viewBox="0 0 42 40"><path d="M3 2 H39 Q41 2 41 4 V28 Q41 30 39 30 H14 L7 38 V30 H3 Q1 30 1 28 V4 Q1 2 3 2Z" fill="#c8c8c8" stroke="#aaa"/><circle cx="14" cy="16" r="2" fill="#fff"/><circle cx="21" cy="16" r="2" fill="#fff"/><circle cx="28" cy="16" r="2" fill="#fff"/></svg>
      <div class="feature-title">NEW IDEAS<small>LOREM IPSUM DOLOR</small></div>
    </div>
    <ul class="links" style="margin-top:22px">
      <li><svg width="8" height="6" viewBox="0 0 8 6"><path d="M0 3H6M4 1L6.5 3L4 5" stroke="#333" fill="none"/></svg>Nam eu nulla. Donec lobortis purus vel</li>
      <li><svg width="8" height="6" viewBox="0 0 8 6"><path d="M0 3H6M4 1L6.5 3L4 5" stroke="#333" fill="none"/></svg>urna. Nunc laoreet lacinia nunc. In volutpat</li>
      <li><svg width="8" height="6" viewBox="0 0 8 6"><path d="M0 3H6M4 1L6.5 3L4 5" stroke="#333" fill="none"/></svg>sodales ipsum. Sed vestibulum. Integer in</li>
      <li><svg width="8" height="6" viewBox="0 0 8 6"><path d="M0 3H6M4 1L6.5 3L4 5" stroke="#333" fill="none"/></svg>ante. Sed posuere ligula rhoncus erat.</li>
      <li><svg width="8" height="6" viewBox="0 0 8 6"><path d="M0 3H6M4 1L6.5 3L4 5" stroke="#333" fill="none"/></svg>Fusce urna dui, sollicitudin ac, Nam eu</li>
    </ul>
  </div>
  <div class="hrule abs"></div>

  <section class="about abs" style="left:26px;top:224px">
    <h2 class="section-title" style="font-weight:400;margin-bottom:22px">About Our Company</h2>
    <p>Lorem ipsum dolor sit amet, consectetur adipiscing elit. In interdum aliquet orci, vitae ornare erat elementum et. Nullam sagittis quam in leo ornare ut gravida turpis eleifend. Morbi eget diam non diam iaculis tristique nec nec sem.</p>
    <p style="margin-bottom:5px">Vestibulum a eros tellus, quis adipiscing neque. Sed varius, risus nec hendrerit pretium, lorem purus euismod risus, tincidunt dictum odio ligula non purus. In volutpat dui a ipsum lobortis rutrum. Pellentesque commodo aliquam pulvinar. In erat risus, molestie vitae porta molestie, pulvinar non justo.</p>
    <span class="more">read more</span>
  </section>

  <section class="blog abs" style="left:567px;top:223px">
    <h2 class="section-title" style="font-weight:400;margin-bottom:21px">Hot from the blog</h2>
    <div class="post">
      <div class="thumb"><div role="img" aria-label="Blue book cover thumbnail" style="background:linear-gradient(135deg,#c9d6f5,#3d64b8)"></div></div>
      <div class="post-text"><h4>Lorem ipsum dolor sit amet</h4><p>Lorem ipsum dolor sit amet, consectetur adipiscing elit. In interdum aliquet orci.</p></div>
    </div>
    <div style="width:239px;height:1px;background:var(--rule);margin:14px 0 15px"></div>
    <div class="post">
      <div class="thumb"><div role="img" aria-label="Glowing orange pumpkin thumbnail" style="background:linear-gradient(160deg,#e8862a,#7a2a08)"></div></div>
      <div class="post-text"><h4>Lorem ipsum dolor sit amet</h4><p>Lorem ipsum dolor sit amet, consectetur adipiscing elit. In interdum aliquet orci.</p></div>
    </div>
  </section>
</main>

<footer class="site-footer abs">
  <div class="quick abs" style="left:136px;top:33px">
    <h3 class="foot-title" style="font-weight:400">QUICK LINKS</h3>
    <ul>
      <li><svg width="6" height="9" viewBox="0 0 6 9"><path d="M0 0L6 4.5L0 9Z" fill="#fff"/></svg>Home</li>
      <li><svg width="6" height="9" viewBox="0 0 6 9"><path d="M0 0L6 4.5L0 9Z" fill="#fff"/></svg>About Us</li>
      <li><svg width="6" height="9" viewBox="0 0 6 9"><path d="M0 0L6 4.5L0 9Z" fill="#fff"/></svg>Services</li>
      <li><svg width="6" height="9" viewBox="0 0 6 9"><path d="M0 0L6 4.5L0 9Z" fill="#fff"/></svg>Blog</li>
      <li><svg width="6" height="9" viewBox="0 0 6 9"><path d="M0 0L6 4.5L0 9Z" fill="#fff"/></svg>Newsletter</li>
      <li><svg width="6" height="9" viewBox="0 0 6 9"><path d="M0 0L6 4.5L0 9Z" fill="#fff"/></svg>Contact Us</li>
    </ul>
  </div>

  <div class="newsletter abs" style="left:398px;top:38px">
    <h3 class="foot-title" style="font-weight:400;margin-left:2px">AS SEEN ON DAILY LEDGER</h3>
    <div class="email" style="margin-top:14px">Enter your email id</div>
    <p class="note" style="margin:14px 0 0 5px">Sed ut perspiciatis unde omnis iste natus error sit voluptatem accusantium</p>
    <div class="submit" style="margin:11px 0 0 6px">Submit</div>
  </div>

  <div class="follow abs" style="left:711px;top:32px">
    <h3 class="foot-title" style="font-weight:400">FOLLOW US</h3>
    <div class="social" style="margin-top:14px">
      <span style="background:#4a6fb5" aria-label="Social profile"></span>
      <span style="background:#3fb4e6" aria-label="Social profile"></span>
      <span style="background:#d9443a" aria-label="Social profile"></span>
    </div>
  </div>
</footer>
<div class="faint-brand abs"><i></i>BREVIK ADVISORY</div>
<div class="bottom-bar abs">© 2014.www.brevikadvisory.com</div>

</body>
</html>
```